Flyer for an IT consultancy firm

We are an IT consultancy firm based in Iceland. We have a website at: www.brimvolt.com where you can get acquainted with our activities.
We require a double-sided flyer in A4 format to be handed out in conferences, trade shows etc. The flyer is basically a summarized overview of our range of services.

The deliverable should incorporate some visual elements that are relevant to our line of business such as:
• computers
• cybersecurity
• networks
Also, it would be nice to have visuals relating to Icelandic geography, to further emphasize our local roots. Some suggested keywords:
• volcano
• aurora borealis
• waterfall
• glacier

NB: the flyer will be printed out, therefore image resolution needs to be high enough to render nicely on paper.
The primary colors would be red, black and white – in line with our logo. But there is freedom to diverge and go for a different color scheme.

The logo should be present on the top front of the flyer. The URL www.brimvolt.com needs to be mentioned prominently, for example at the bottom of the page.

Examples of design we like:
• https://www.pixelbazaar.net/design/24252027
• https://www.pixelbazaar.net/design/24291120

Attached:
• the text for the brochure in PDF format
• our logo in vector format

IT, software, cybersecurity

EB3D1F
EC4F4E
F09395
F8D3D4
FCEDEE

• existing logo, and visuals related to computer, networks etc
• Icelandic geography/landscapes

```html
<!DOCTYPE html>
<html lang="en">
<head>
<meta charset="utf-8">
<title>Brimvolt ehf – IT Services Flyer</title>
<link href="https://fonts.googleapis.com/css2?family=Montserrat:wght@300;400;500;600;700;800&display=swap" rel="stylesheet">
<style>
  :root {
    --red: #9e1c20;
    --red-bright: #b8252a;
    --navy: #0e2440;
    --ink: #141414;
    --body: #3b3b3b;
    --paper: #ffffff;
    --panel: #f2f3f5;
    --stage: #6b7880;
  }
  * { margin: 0; padding: 0; box-sizing: border-box; }
  html, body { width: 1200px; height: 1200px; overflow: hidden; }
  body { background: var(--stage); font-family: "Montserrat", sans-serif; position: relative; }

  .flyer {
    position: absolute; left: 177px; top: 8px;
    width: 846px; height: 1185px;
    background: var(--panel); overflow: hidden;
  }

  .masthead {
    position: absolute; left: 0; top: 0; width: 100%; height: 112px;
    background: var(--paper);
    display: flex; align-items: center; justify-content: center; gap: 12px;
  }
  .brand-dot { width: 54px; height: 54px; border-radius: 50%; background: var(--red); }
  .brand-name { font-weight: 800; font-size: 36px; color: var(--ink); letter-spacing: 0.5px; }

  .hero {
    position: absolute; left: 0; top: 112px; width: 100%; height: 209px;
    background:
      linear-gradient(to bottom, rgba(14,36,64,0) 40%, rgba(158,28,32,0.95) 100%),
      linear-gradient(100deg, #7a3418 0%, #40506a 22%, #13294a 45%, #14284a 75%, #1e4d6e 100%);
    text-align: center; color: #fff;
  }
  .hero-company { position: absolute; top: 113px; width: 100%; font-weight: 300; font-size: 40px; letter-spacing: 0.5px; }
  .hero-title { position: absolute; top: 156px; width: 100%; font-weight: 800; font-size: 40px; letter-spacing: -0.3px; }

  .intro {
    position: absolute; left: 0; top: 321px; width: 100%; height: 74px;
    background: var(--navy); color: #fff;
    font-size: 12px; line-height: 16.5px; text-align: center;
    padding: 11px 44px 0; letter-spacing: -0.1px;
  }

  .service { position: absolute; width: 380px; }
  .service .icon {
    position: absolute; left: 0; top: 0; width: 26px; height: 26px; border-radius: 50%;
    background: var(--red); box-shadow: 0 0 0 2px var(--paper), 0 0 0 3px var(--red);
  }
  .service .rail {
    position: absolute; left: 12px; top: 36px; bottom: 0;
    border-left: 2px dotted #8a8a8a;
  }
  .service .content { margin-left: 37px; width: 318px; }
  .service h2 { font-weight: 700; font-size: 18.5px; line-height: 22px; color: var(--ink); text-transform: uppercase; padding-top: 3px; letter-spacing: -0.4px; white-space: nowrap; }
  .service p { margin-top: 9px; font-size: 12px; line-height: 15.2px; color: var(--body); text-align: justify; letter-spacing: -0.15px; }
  .service .tagline {
    margin: 9px 0 0 -6px; width: 334px; padding: 4px 6px;
    background: linear-gradient(90deg, var(--red) 0%, var(--red-bright) 60%, rgba(184,37,42,0) 100%);
    color: #fff; font-weight: 600; font-size: 12px; line-height: 13.5px; border-radius: 3px 0 0 3px;
  }
  .col-left { left: 41px; }
  .col-right { left: 446px; }
  .col-right .tagline { margin-left: 0; padding-left: 9px; }

  .contact-lead {
    position: absolute; left: 0; top: 1056px; width: 431px; height: 56px;
    background: var(--navy); border-top-right-radius: 6px;
    color: #fff; font-weight: 600; font-size: 15.5px; line-height: 19px; padding: 8px 0 0 55px;
  }
  .phone-band {
    position: absolute; left: 0; top: 1111px; width: 431px; height: 74px;
    background: var(--red); color: #fff;
    display: flex; align-items: center; gap: 14px; padding-left: 66px;
    font-weight: 700; font-size: 37px;
  }
  .web-band {
    position: absolute; left: 431px; top: 1111px; right: 0; height: 74px;
    background: var(--navy); color: #fff; font-size: 15px;
    display: flex; align-items: center; padding-left: 20px; gap: 36px;
  }
  .web-band span { display: flex; align-items: center; gap: 10px; }
</style>
</head>
<body>
<main class="flyer">
  <header class="masthead">
    <div class="brand-dot"></div>
    <div class="brand-name">BRIMVOLT</div>
  </header>

  <section class="hero" role="img" aria-label="Photo of a server room corridor blending into a glowing digital globe network">
    <div class="hero-company">BRIMVOLT EHF</div>
    <h1 class="hero-title">YOUR ICELANDIC IT PARTNER</h1>
  </section>

  <p class="intro">Step into a world of comprehensive IT solutions tailored to your unique needs. Our services, available on a contract or as-needed basis, are designed to empower your business and equip you with the tools you need to succeed. More than just a list of offerings, they’re a commitment to quality, a dedication to innovation, and a promise of reliability.</p>

  <article class="service col-left" style="top:422px;height:205px">
    <div class="icon"></div><div class="rail"></div>
    <div class="content">
      <h2>Software development and<br>integration services</h2>
      <p>We specialize in custom software development across different platforms (server, desktop, embedded systems). We are open source software advocates, and leverage decades of experience to deliver innovative and cost-effective solutions tailored to your needs.</p>
      <div class="tagline">Let’s build the perfect software solution for you.</div>
    </div>
  </article>

  <article class="service col-right" style="top:422px;height:205px">
    <div class="icon"></div><div class="rail"></div>
    <div class="content">
      <h2>Systems<br>administration</h2>
      <p>Are you having trouble with your IT infrastructure and in need of qualified personnel to take care of them? Or do you simply need a watchful and expert eye to ensure your systems keep running smoothly? We provide on-site and remote sysadmin services to manage your systems and bring you peace of mind.</p>
      <div class="tagline">Take back control.</div>
    </div>
  </article>

  <article class="service col-left" style="top:637px;height:220px">
    <div class="icon"></div><div class="rail"></div>
    <div class="content">
      <h2>Infrastructure monitoring<br>services</h2>
      <p>Do you know what is really going on inside your systems? We leverage leading open source monitoring solutions to bring visibility to your infrastructure. Monitor your systems proactively to ensure that they remain healthy at all times. Collect logs in real time and be notified when problems occur or warnings are raised.</p>
      <div class="tagline">Fix issues before they become problems.</div>
    </div>
  </article>

  <article class="service col-right" style="top:637px;height:220px">
    <div class="icon"></div><div class="rail"></div>
    <div class="content">
      <h2>Automation</h2>
      <p>Because you need effective tools to grow and prosper, it is essential that your IT systems align with your operational needs. We offer a comprehensive review of your business and IT environment so as to optimize the means already at your disposal. We streamline your workflow and develop new tools as needed, to make your IT systems work harder for you.</p>
      <div class="tagline">Let us automate the boring stuff for you.</div>
    </div>
  </article>

  <article class="service col-left" style="top:865px;height:170px">
    <div class="icon"></div><div class="rail"></div>
    <div class="content">
      <h2>Technology assessment<br>services</h2>
      <p>Unsure about which tools are right for you or what IT strategy to pursue to help your business grow? We conduct market research and perform technical evaluations of software and hardware products to determine the best solutions for your company</p>
      <div class="tagline">Let’s empower your business with leading-edge solutions.</div>
    </div>
  </article>

  <article class="service col-right" style="top:865px;height:180px">
    <div class="icon"></div><div class="rail"></div>
    <div class="content">
      <h2>Security services</h2>
      <p>We understand the importance of security in today’s digital landscape. That’s why we offer comprehensive security services, including network audits to find and remedy flaws before they can be exploited to your disadvantage. We perform a thorough review of your IT environment to identify and remediate the weak spots, in order to keep your business secure, protect your assets and your reputation. Let’s raise your security posture to the highest standards, so that you don't become the next victim - or headline.</p>
      <div class="tagline">Bring the good guys in to keep the bad guys out.</div>
    </div>
  </article>

  <div class="contact-lead">Get In Touch With Us Today To Discuss<br>Your It Needs In Strict Confidence.</div>

  <div class="phone-band">
    <svg width="40" height="40" viewBox="0 0 40 40" aria-hidden="true">
      <circle cx="20" cy="20" r="19" fill="#fff"/>
      <path d="M13 10c1.5-1 3-.5 3.6.8l1.8 3.6c.5 1-.2 2-1 2.6l-1 .8c1 2.6 3 4.8 5.6 6l.9-1c.7-.8 1.7-1.3 2.7-.8l3.5 1.9c1.2.6 1.5 2.2.6 3.4-1.6 2-4 2.6-6.3 1.6-5.2-2.3-8.8-6.2-10.6-11.5-.7-2.2.2-4.3 2.2-5.4z" fill="var(--red)"/>
    </svg>
    +354 555 0192
  </div>

  <div class="web-band">
    <span>
      <svg width="18" height="18" viewBox="0 0 20 20" fill="none" stroke="#fff" stroke-width="1.3" aria-hidden="true">
        <circle cx="10" cy="10" r="8.5"/><ellipse cx="10" cy="10" rx="3.8" ry="8.5"/>
        <line x1="1.5" y1="10" x2="18.5" y2="10"/><line x1="3" y1="5.5" x2="17" y2="5.5"/><line x1="3" y1="14.5" x2="17" y2="14.5"/>
      </svg>
      www.brimvolt.com
    </span>
    <span>
      <svg width="18" height="13" viewBox="0 0 18 13" aria-hidden="true">
        <rect width="18" height="13" rx="1" fill="#fff"/>
        <path d="M1 1.5l8 6 8-6" fill="none" stroke="var(--navy)" stroke-width="1.4"/>
      </svg>
      info@brimvolt.com
    </span>
  </div>
</main>
</body>
</html>
```